Legal Consultant: Book cover for "Silver Ridge Transitions" in Australia.

This project is for the desiign of the front cover of a book t be published in perfect bond (A5) and as an eBook.

The target readers are Australian law firm partners.

I am a lawyer and senior legal recruitment consultant specialisng in the recruitment of law firm partners. I have written a short book that advises law firm partners how to make a lateral move to another law firm. It's simply about recruitment at a senior level. The book sets out the steps to maximise the partner's opportunity to engage the services of a senior legal recruitment consultant and then identify suitable law firms, interview techniques and preparation. A key element in the book is the preparation of various documents to submit to potential law firms eg CV, business plan, financial performance.

I know the eBook design has to 'grab" the reader so the title will need to jump out at the reader.

Target Market(s)

Senior law firm partners in Australia

Industry/Entity Type

Graphic Design

Requirements
Must have
• The cover must also be suitable for eBook publication. Therefore it must stand out from competitive publications.
Nice to have
• A design suitable for senior professional services executves.
Should not have
• No cliches eg shaking hands, two men in suits, judge's gavel etc

```html
<!DOCTYPE html>
<html lang="en">
<head>
<meta charset="utf-8">
<title>A Partner's Guide – Book Cover</title>
<link href="https://fonts.googleapis.com/css2?family=Bodoni+Moda:wght@500;700;800&display=swap" rel="stylesheet">
<style>
  :root {
    --page-bg: #ffffff;
    --cover-deep: #0f1a24;
    --cover-mid: #2a4256;
    --cover-light: #3d5a70;
    --title-cream: #f7ecd2;
    --subtitle-white: #ffffff;
    --spine-text: #f2f2f2;
    --isbn-bg: #ffffff;
    --isbn-text: #111111;
    --scene-dark: rgba(18, 26, 34, 0.55);
    --scene-ivory: rgba(200, 178, 140, 0.28);
  }
  * { margin: 0; padding: 0; box-sizing: border-box; }
  html, body {
    width: 1200px;
    height: 857px;
    overflow: hidden;
    background: var(--page-bg);
  }
  .canvas {
    position: relative;
    width: 1200px;
    height: 857px;
  }
  .cover-wrap {
    position: absolute;
    left: 69px;
    top: 88px;
    width: 1083px;
    height: 748px;
    overflow: hidden;
    background:
      radial-gradient(ellipse 45% 40% at 30% 35%, var(--cover-light) 0%, transparent 100%),
      radial-gradient(ellipse 60% 55% at 70% 45%, var(--cover-mid) 0%, transparent 100%),
      linear-gradient(180deg, #1c2d3c 0%, var(--cover-mid) 40%, #1a2a38 75%, var(--cover-deep) 100%);
    font-family: "Bodoni Moda", "Times New Roman", serif;
  }
  .spine-title, .spine-author {
    position: absolute;
    left: 540px;
    writing-mode: vertical-rl;
    color: var(--spine-text);
    white-space: nowrap;
    transform: translateX(-50%);
  }
  .spine-title {
    top: 52px;
    font-size: 15px;
    font-weight: 500;
    letter-spacing: 0.5px;
  }
  .spine-author {
    top: 444px;
    font-size: 13.5px;
    font-weight: 700;
    letter-spacing: 0.4px;
  }
  .front {
    position: absolute;
    left: 562px;
    top: 0;
    width: 521px;
    height: 748px;
  }
  .title {
    position: absolute;
    top: 44px;
    left: 0;
    width: 521px;
    text-align: center;
    color: var(--title-cream);
    font-weight: 800;
    font-size: 63px;
    line-height: 82px;
    letter-spacing: 1px;
    text-shadow: 3px 4px 4px rgba(0,0,0,0.6);
  }
  .scene {
    position: absolute;
    left: 0;
    top: 188px;
    width: 521px;
    height: 284px;
    background: linear-gradient(180deg, transparent 0%, var(--scene-ivory) 45%, var(--scene-dark) 80%, transparent 100%);
  }
  .subtitle {
    position: absolute;
    top: 500px;
    left: 0;
    width: 521px;
    text-align: center;
    color: var(--subtitle-white);
    font-weight: 700;
    font-size: 40px;
    line-height: 55px;
    letter-spacing: 1px;
    word-spacing: 6px;
    text-shadow: 2px 3px 3px rgba(0,0,0,0.6);
  }
  .author {
    position: absolute;
    top: 692px;
    left: 0;
    width: 521px;
    text-align: center;
    color: var(--title-cream);
    font-weight: 700;
    font-size: 21px;
    letter-spacing: 0.4px;
  }
  .isbn-box {
    position: absolute;
    left: 11px;
    top: 640px;
    width: 221px;
    height: 79px;
    background: var(--isbn-bg);
    color: var(--isbn-text);
    text-align: center;
    font-weight: 700;
    font-size: 15px;
    padding-top: 10px;
  }
</style>
</head>
<body>
<div class="canvas">
  <section class="cover-wrap" aria-label="Book cover: A Partner's Guide">
    <div class="spine-title">A PARTNER’S GUIDE</div>
    <div class="spine-author">Daniel Hartley LL.B Barrister-at-Law</div>

    <div class="front">
      <h1 class="title">A PARTNER’S<br>GUIDE</h1>
      <div class="scene" role="img" aria-label="Photograph of black and ivory chess pieces on a reflective surface, one ivory king toppled among them"></div>
      <h2 class="subtitle">MANAGING&nbsp; YOUR<br>LATERAL MOVE</h2>
      <p class="author">Daniel Hartley LL.B Barrister-at-Law</p>
    </div>

    <div class="isbn-box">ISBN</div>
  </section>
</div>
</body>
</html>
```